Dryer Vent Cleaning Postcard Design

We need a postcard design for Flue Wranglers, a company that specializes in dryer vent cleaning, repairs and upgrades. Dryer vents need periodic cleaning to avoid lint clogging, dryer malfunction, long dry times and even a house fire. This card will be sent to residential and businesses prospects to introduce them to our services and the importance of maintaining their dryer vents. Our website is @ fluewrangling.com and provides information about our services, photos of our work and our general color scheme (purple/orange). Final print size will be 5x7 horizontal.

Target Market(s)

homeowners and business owners (spas, salons, grooming, gyms, laundrymats, etc)

Requirements
Must have
• Reduce the risk of fire
shortened dry times
lower energy consumption
18000 dryer fires caused in the US per year
Nice to have
• Does your dryer take too long to dry?

```html
<!DOCTYPE html>
<html lang="en">
<head>
<meta charset="utf-8">
<title>Flue Wranglers Postcard</title>
<link href="https://fonts.googleapis.com/css2?family=Marcellus&family=Lato:wght@400;700&display=swap" rel="stylesheet">
<style>
  :root {
    --backdrop: #6b6b6b;
    --paper: #ffffff;
    --paper-warm: #f7f4ee;
    --purple: #35286e;
    --orange: #f0462a;
    --ink: #1c1c1c;
    --stamp: #d4d4d4;
    --rule: #c9c9c9;
    --serif: 'Marcellus', serif;
    --sans: 'Lato', sans-serif;
  }
  * { box-sizing: border-box; margin: 0; padding: 0; }
  html, body { width: 1200px; height: 900px; overflow: hidden; }
  body { background: var(--backdrop); position: relative; font-family: var(--sans); }

  .postcard {
    position: absolute;
    width: 560px; height: 400px;
    overflow: hidden;
    box-shadow: 0 6px 18px rgba(0,0,0,.35);
  }
  .postcard--front { left: 26px; top: 250px; background: var(--paper); }
  .postcard--back { left: 614px; top: 250px; background: var(--paper-warm); }
  .swoosh-layer { position: absolute; inset: 0; width: 100%; height: 100%; }

  .placeholder { position: absolute; }
  .vent-photo {
    left: 200px; top: 0; width: 360px; height: 150px;
    background: linear-gradient(180deg, #d8d6d2 0%, #ecebe8 60%, rgba(255,255,255,0) 100%);
    opacity: .8;
  }
  .technician-art {
    left: 40px; top: 40px; width: 170px; height: 345px;
    border-radius: 40px 40px 10px 10px;
    background: linear-gradient(180deg, #8a7560 0%, #a38b71 50%, #6d5a48 100%);
  }

  .headline {
    position: absolute; left: 215px; top: 58px; width: 330px;
    text-align: center; font-family: var(--serif); font-weight: 400; color: var(--purple); line-height: 1.1;
  }
  .headline__lead { font-size: 33px; display: block; }
  .headline__accent { font-size: 25px; color: var(--orange); display: block; margin-top: 2px; }
  .headline__end { font-size: 30px; display: block; margin-top: 2px; }

  .badge-name {
    position: absolute; left: 311px; top: 273px; width: 68px;
    text-align: center; font-family: var(--serif); font-size: 12px; color: var(--purple); line-height: 1.15;
  }

  .contact { position: absolute; font-family: var(--serif); color: var(--purple); }
  .contact--front { right: 44px; top: 348px; text-align: right; }
  .contact__phone { font-size: 17px; display: block; line-height: 1.1; }
  .contact__web { font-size: 11px; letter-spacing: 2.5px; display: block; margin-top: 4px; color: var(--ink); }

  .attic-photo {
    left: 0; top: 0; width: 300px; height: 190px;
    background: linear-gradient(180deg, #b88e6c 0%, #c9a98a 45%, rgba(247,244,238,0) 100%);
  }
  .benefits {
    position: absolute; left: 28px; top: 196px; width: 165px;
    list-style: none; font-size: 11px; color: var(--ink); line-height: 1.2;
  }
  .benefits li { position: relative; padding-left: 22px; margin-bottom: 6px; }
  .benefits li::before {
    content: ""; position: absolute; left: 0; top: 2px;
    width: 10px; height: 10px; border-radius: 50%; background: var(--ink);
  }
  .contact--back { left: 28px; top: 305px; color: var(--ink); }
  .contact--back .contact__phone { font-size: 15px; }
  .contact--back .contact__web { font-size: 10px; margin-top: 3px; }

  .stamp-box { position: absolute; right: 40px; top: 36px; width: 56px; height: 56px; background: var(--stamp); }
  .address-lines { position: absolute; left: 335px; top: 230px; width: 190px; }
  .address-lines span { display: block; height: 1px; background: var(--rule); margin-bottom: 30px; }
</style>
</head>
<body>

<section class="postcard postcard--front">
  <div class="placeholder vent-photo" role="img" aria-label="Faded photo of a hand reaching into a ceiling vent"></div>

  <svg class="swoosh-layer" viewBox="0 0 560 400" aria-hidden="true">
    <path d="M0 262 C100 275 170 360 240 368 C330 378 430 246 560 232 L560 280 C470 282 390 310 300 370 L275 400 L200 400 C150 370 90 310 0 305 Z" fill="#f0462a"/>
    <path d="M0 218 C100 228 170 316 240 322 C330 330 430 196 560 180 L560 226 C430 240 330 370 240 362 C170 356 100 268 0 256 Z" fill="#35286e"/>
    <circle cx="250" cy="335" r="38" fill="#fff" stroke="#35286e" stroke-width="5"/>
    <circle cx="250" cy="335" r="31" fill="#b7b1a8"/>
    <circle cx="345" cy="285" r="46" fill="#fff" stroke="#f0462a" stroke-width="5"/>
    <circle cx="345" cy="285" r="38" fill="#fff" stroke="#35286e" stroke-width="4"/>
    <circle cx="470" cy="226" r="46" fill="#fff" stroke="#35286e" stroke-width="5"/>
    <circle cx="470" cy="226" r="39" fill="#8f857a"/>
  </svg>

  <div class="placeholder technician-art" role="img" aria-label="Illustrated technician holding a vent cleaning brush and vacuum hose"></div>

  <h1 class="headline">
    <span class="headline__lead">DOES YOUR DRYER</span>
    <span class="headline__accent">TAKE TOO LONG</span>
    <span class="headline__end">TO DRY?</span>
  </h1>

  <p class="badge-name">Flue Wranglers</p>

  <p class="contact contact--front">
    <span class="contact__phone">CALL-+1 555-014-2273</span>
    <span class="contact__web">WWW.FLUEWRANGLING.COM</span>
  </p>
</section>

<section class="postcard postcard--back">
  <div class="placeholder attic-photo" role="img" aria-label="Photo of attic insulation with a dryer vent duct"></div>

  <svg class="swoosh-layer" viewBox="0 0 560 400" aria-hidden="true">
    <path d="M300 0 L350 0 C300 60 250 130 255 210 C260 300 330 350 380 400 L305 400 C250 350 205 300 205 210 C205 120 260 50 300 0 Z" fill="#f0462a"/>
    <path d="M350 0 L395 0 C340 60 295 130 300 210 C305 300 370 350 425 400 L380 400 C330 350 262 300 257 210 C252 130 300 60 350 0 Z" fill="#35286e"/>
    <circle cx="252" cy="215" r="50" fill="#fff" stroke="#f0462a" stroke-width="5"/>
    <rect x="222" y="192" width="60" height="48" rx="4" fill="#d9d6d0" role="img" aria-label="Illustration of a dryer clogged with lint"/>
  </svg>

  <ul class="benefits">
    <li>Reduce the risk of fire</li>
    <li>shortened dry times</li>
    <li>lower energy consumption</li>
    <li>18000 dryer fires caused in the US per year</li>
  </ul>

  <p class="contact contact--back">
    <span class="contact__phone">CALL-+1 555-014-2273</span>
    <span class="contact__web">WWW.FLUEWRANGLING.COM</span>
  </p>

  <div class="stamp-box"></div>
  <div class="address-lines"><span></span><span></span><span></span></div>
</section>

</body>
</html>
```